Framework, Visual of our 6 phase process of working with clients

We are an epidemiology consulting firm and need a visual that describes our 6 phase process of how our clients work with us. This will be used in marketing and sales to help potential client understand what to expect when working with us. A visual of our framework will also help us demonstrate authority and more easily explain our process in the sales process. Please message me if you have any questions.

Include our website somewhere: DrMBFolwell.com

Target Market(s)

Large Nonprofit organization leaders

Industry/Entity Type

Health, Public Health, Epidemiology

Font styles to use
Serif

Requirements
Must have
• Please use brand colors: #56588C, #F28444 you can also use #F2E088, #F24C27, #0D0D0D

```html
<!DOCTYPE html>
<html lang="en">
<head>
<meta charset="utf-8">
<title>Six-Phase Partnership</title>
<link rel="stylesheet" href="https://fonts.googleapis.com/css2?family=Teko:wght@500;600&family=Mukta:wght@400;600;700&display=swap">
<style>
  :root{
    --sky:#21a3d6;
    --white:#ffffff;
    --green:#00b80e;
    --orange:#f39a26;
    --purple:#9b06b8;
    --red:#c00027;
    --navy:#15608e;
    --teal:#00b8c8;
    --link:#15608e;
    --ink:#0d0d0d;
  }
  *{box-sizing:border-box;margin:0;padding:0}
  html,body{width:1200px;height:1200px;overflow:hidden}
  body{background:var(--sky);font-family:"Mukta",sans-serif;position:relative}

  .masthead{position:absolute;left:0;top:0;width:1200px;height:132px;background:var(--green);
    display:flex;align-items:center;justify-content:center}
  .masthead h1{font-family:"Teko",sans-serif;font-weight:600;color:var(--white);
    font-size:120px;line-height:1;letter-spacing:1px;padding-top:16px}

  .phase{position:absolute;top:227px;width:109px;height:366px;background:var(--white);border-radius:5px}
  .phase--1{left:163px;--c:var(--orange);--dark:#b9612a;--grip:#c46b2c;--txt:#c0622a}
  .phase--2{left:315px;--c:var(--green);--dark:#0b6a1f;--grip:#0b6a1f;--txt:#0b6a1f}
  .phase--3{left:469px;--c:var(--purple);--dark:#6d0a7a;--grip:#6d0a7a;--txt:#6d0a7a}
  .phase--4{left:622px;--c:var(--red);--dark:#7e0018;--grip:#7e0018;--txt:#8a0022}
  .phase--5{left:775px;--c:var(--navy);--dark:#0c3f60;--grip:#0c3f60;--txt:#0d4a70}
  .phase--6{left:928px;--c:var(--teal);--dark:#0c6e72;--grip:#0c6e72;--txt:#0c6e72}

  .phase__strap{position:absolute;left:47px;top:-95px;width:15px;height:100px;background:var(--c)}
  .phase__buckle{position:absolute;left:45px;top:-31px;width:19px;height:11px;background:var(--dark);border-radius:2px}
  .phase__cap{position:absolute;left:10px;top:3px;width:89px;height:67px;background:var(--c);
    border-radius:0 0 45px 45px;display:flex;align-items:flex-end;justify-content:center;padding-bottom:13px;
    color:var(--white);font-weight:600;font-size:11px;letter-spacing:.3px}
  .phase__hand{position:absolute;left:40px;top:-20px;width:29px;height:34px;background:var(--white);border-radius:6px 6px 3px 3px}
  .phase__hand::after{content:"";position:absolute;left:-2px;bottom:-4px;width:33px;height:7px;background:var(--grip);border-radius:2px}
  .phase__title{position:absolute;left:0;top:74px;width:100%;height:28px;display:flex;align-items:center;justify-content:center;
    text-align:center;color:var(--c);font-size:10.5px;line-height:13px}
  .phase__band{position:absolute;left:0;top:112px;width:100%;height:30px;background:var(--c);
    display:flex;align-items:center;justify-content:center;text-align:center;
    font-family:"Teko",sans-serif;font-weight:500;color:var(--white);font-size:9.5px;line-height:10.5px;letter-spacing:.3px;padding-top:2px;text-transform:uppercase}
  .phase__intro{position:absolute;left:6px;right:6px;top:144px;text-align:center;color:var(--txt);font-size:7px;line-height:7.6px}
  .phase__list{position:absolute;left:3px;right:2px;top:157px;list-style:none;color:var(--txt);font-size:9.3px;line-height:13px}
  .phase__list li{position:relative;padding-left:8px;margin-bottom:13px}
  .phase__list li::before{content:"";position:absolute;left:1px;top:5px;width:4px;height:4px;border-radius:50%;background:var(--txt)}
  .phase--3 .phase__list{top:175px}

  .phase__arm{position:absolute;left:13px;top:366px;width:11px;height:28px;background:var(--white)}
  .phase__arm::after{content:"";position:absolute;left:0;top:17px;width:43px;height:11px;background:var(--white)}
  .phase__cuff{position:absolute;left:54px;top:383px;width:7px;height:13px;background:var(--c)}
  .phase__point{position:absolute;left:61px;top:381px;width:36px;height:15px;background:var(--dark);border-radius:3px 8px 8px 3px}

  .why-heading{position:absolute;left:0;top:650px;width:1200px;text-align:center;font-family:"Teko",sans-serif;
    font-weight:600;color:var(--white);font-size:66px;line-height:60px}

  .reason{position:absolute;top:719px;width:172px;height:157px;border-radius:6px;overflow:hidden}
  .reason--expertise{left:194px;--c:var(--green);--head:#067a12}
  .reason--impact{left:410px;--c:var(--purple);--head:#6d0a7a}
  .reason--innovation{left:623px;--c:var(--red);--head:#7e0018}
  .reason--partnership{left:840px;--c:var(--navy);--head:#0c3a5c}
  .reason{background:var(--c)}
  .reason h3{height:37px;background:var(--head);color:var(--white);font-family:"Teko",sans-serif;font-weight:600;
    font-size:30px;line-height:42px;text-align:center;letter-spacing:.3px}
  .reason p{padding:9px 10px 0;color:var(--white);font-weight:600;font-size:10.6px;line-height:19.8px}

  .cta-heading{position:absolute;left:0;top:918px;width:1200px;text-align:center;font-family:"Teko",sans-serif;
    font-weight:600;color:var(--white);font-size:46px;line-height:46px;letter-spacing:.3px}

  .contact{position:absolute;left:396px;top:978px;width:414px;height:163px;background:var(--white);border-radius:26px;
    padding:11px 22px 0 23px}
  .contact p{font-weight:700;color:var(--ink);font-size:21.5px;line-height:31px}
  .contact a{display:block;font-weight:700;color:var(--link);font-size:21.5px;line-height:31px;text-decoration:none}
</style>
</head>
<body>
  <header class="masthead"><h1>SIX-PHASE PARTNERSHIP</h1></header>

  <section class="phase phase--1">
    <div class="phase__strap"></div><div class="phase__buckle"></div>
    <div class="phase__cap">PHASE 1</div>
    <div class="phase__hand" role="img" aria-label="Hand holding the phase card"></div>
    <div class="phase__title">Discovery &amp;<br>Vision Alignment</div>
    <div class="phase__band">Building<br>the foundation for success</div>
    <ul class="phase__list">
      <li>Deep-dive exploration of your organization's unique challenges and opportunities</li>
      <li>Strategic alignment of goals and expectations</li>
      <li>Custom-tailored solution design</li>
      <li>Clear roadmap development with defined milestones</li>
    </ul>
    <div class="phase__arm"></div><div class="phase__cuff"></div>
    <div class="phase__point" role="img" aria-label="Hand pointing to the next phase"></div>
  </section>

  <section class="phase phase--2">
    <div class="phase__strap"></div><div class="phase__buckle"></div>
    <div class="phase__cap">PHASE 2</div>
    <div class="phase__hand" role="img" aria-label="Hand holding the phase card"></div>
    <div class="phase__title">Partnership Launch</div>
    <div class="phase__band">Setting the stage<br>for excellence</div>
    <ul class="phase__list">
      <li>Formation of dedicated project team</li>
      <li>Establishment of collaborative workflow</li>
      <li>Comprehensive data gathering</li>
      <li>Strategic timeline planning</li>
      <li>Stakeholder engagement and vision capture</li>
    </ul>
    <div class="phase__arm"></div><div class="phase__cuff"></div>
    <div class="phase__point" role="img" aria-label="Hand pointing to the next phase"></div>
  </section>

  <section class="phase phase--3">
    <div class="phase__strap"></div><div class="phase__buckle"></div>
    <div class="phase__cap">PHASE 3</div>
    <div class="phase__hand" role="img" aria-label="Hand holding the phase card"></div>
    <div class="phase__title">Expert Execution</div>
    <div class="phase__band">Where science<br>meets service</div>
    <p class="phase__intro">Our specialized team begins the transformation process:</p>
    <ul class="phase__list">
      <li>In-depth research and analysis</li>
      <li>Content development and refinement</li>
      <li>Data interpretation and visualization</li>
      <li>Plain language translation of complex health information</li>
    </ul>
    <div class="phase__arm"></div><div class="phase__cuff"></div>
    <div class="phase__point" role="img" aria-label="Hand pointing to the next phase"></div>
  </section>

  <section class="phase phase--4">
    <div class="phase__strap"></div><div class="phase__buckle"></div>
    <div class="phase__cap">PHASE 4</div>
    <div class="phase__hand" role="img" aria-label="Hand holding the phase card"></div>
    <div class="phase__title">Collaborative<br>Refinement</div>
    <div class="phase__band">Ensuring<br>perfect alignment</div>
    <ul class="phase__list">
      <li>Presentation of initial frameworks</li>
      <li>Interactive feedback sessions</li>
      <li>Draft review and optimization</li>
      <li>Stakeholder input integration</li>
    </ul>
    <div class="phase__arm"></div><div class="phase__cuff"></div>
    <div class="phase__point" role="img" aria-label="Hand pointing to the next phase"></div>
  </section>

  <section class="phase phase--5">
    <div class="phase__strap"></div><div class="phase__buckle"></div>
    <div class="phase__cap">PHASE 5</div>
    <div class="phase__hand" role="img" aria-label="Hand holding the phase card"></div>
    <div class="phase__title">Impact Delivery</div>
    <div class="phase__band">Bringing vision<br>to reality</div>
    <ul class="phase__list">
      <li>Final deliverable presentation</li>
      <li>Implementation support</li>
      <li>Knowledge transfer</li>
      <li>Impact measurement framework</li>
    </ul>
    <div class="phase__arm"></div><div class="phase__cuff"></div>
    <div class="phase__point" role="img" aria-label="Hand pointing to the next phase"></div>
  </section>

  <section class="phase phase--6">
    <div class="phase__strap"></div><div class="phase__buckle"></div>
    <div class="phase__cap">PHASE 6</div>
    <div class="phase__hand" role="img" aria-label="Hand holding the phase card"></div>
    <div class="phase__title">Evolution &amp; Growth</div>
    <div class="phase__band">Sustaining<br>long-term success</div>
    <ul class="phase__list">
      <li>Project success celebration</li>
      <li>Future opportunities exploration</li>
      <li>Partnership evolution planning</li>
      <li>Continuous improvement recommendations</li>
    </ul>
    <div class="phase__arm"></div><div class="phase__cuff"></div>
    <div class="phase__point" role="img" aria-label="Hand pointing onward"></div>
  </section>

  <h2 class="why-heading">WHY PARTNER WITH US?</h2>

  <article class="reason reason--expertise">
    <h3>EXPERTISE :</h3>
    <p>Our diverse team of innovative global public health professionals, specialized in epidemiology and health communication</p>
  </article>
  <article class="reason reason--impact">
    <h3>IMPACT :</h3>
    <p>Proven track record of transforming complex health data into accessible information</p>
  </article>
  <article class="reason reason--innovation">
    <h3>INNOVATION :</h3>
    <p>Custom solutions tailored to BIPOC community needs</p>
  </article>
  <article class="reason reason--partnership">
    <h3>PARTNERSHIP :</h3>
    <p>Collaborative approach ensuring lasting results</p>
  </article>

  <h2 class="cta-heading">READY TO TRANSFORM YOUR HEALTH COMMUNICATION?</h2>

  <div class="contact">
    <p>Contact us to begin your journey toward more effective, equitable health communication.</p>
    <a href="mailto:support@drmbfolwell.com">support@drmbfolwell.com</a>
  </div>
</body>
</html>
```